Need a website for our company

We need a website for our company to showcase all our work for customers to see.
We do all phases of home improvement:
Dormers/Extensions
Basement Remodel
Masonry/Concrete/Pavers/Asphalt
Cultured Stone Veneer
Kitchens
Bathrooms
Pool designs
Outdoor Bathroom
Outdoor Kitchens
Tile work
For reference, something similar to this website: https://brightoakrenovations.example/
Target Market(s)
We are trying to target homeowners.
Coding
Number of Pages Required
Look and feel

```html
<!DOCTYPE html>
<html lang="en">
<head>
<meta charset="utf-8">
<title>Harlow &amp; Sons Construction Inc</title>
<link rel="stylesheet" href="https://fonts.googleapis.com/css2?family=Montserrat:wght@400;500;600;700&family=Open+Sans:wght@400;600;700&display=swap">
<style>
:root{
  --ink:#111111;
  --black:#000000;
  --white:#ffffff;
  --soft:#f2f2f2;
  --grey:#6b6b6b;
  --line:#d6d6d6;
  --star:#f2b705;
  --navy:#1f2f4a;
  --hero-a:#6b4a2e;
  --hero-b:#a8835b;
}
*{box-sizing:border-box;margin:0;padding:0}
html,body{width:1200px;height:5132px;overflow:hidden}
body{font-family:"Open Sans",Arial,sans-serif;color:var(--ink);background:var(--white);position:relative}
.head{font-family:"Montserrat",Arial,sans-serif}
section,header,footer{position:absolute;left:0;width:1200px}
.abs{position:absolute}
.btn-dark{position:absolute;background:var(--ink);color:var(--white);font-family:"Montserrat",Arial,sans-serif;display:flex;align-items:center;justify-content:center}
svg.ico{display:block}

/* header */
.site-header{top:0;height:108px;background:var(--white)}
.brand{position:absolute;display:flex;align-items:center;gap:10px;font-family:"Montserrat",Arial,sans-serif;font-weight:700;color:var(--ink);white-space:nowrap}
.brand-square{width:14px;height:14px;background:var(--ink);flex:none}
.site-header .brand{left:124px;top:42px;font-size:13px;letter-spacing:.5px}
.nav{position:absolute;right:128px;top:38px;display:flex;align-items:center;font-family:"Montserrat",Arial,sans-serif;font-size:13px;font-weight:500}
.nav a{color:var(--ink);text-decoration:none;padding:0 12px;border-right:1px solid var(--ink);line-height:30px}
.nav a:last-of-type{border-right:none}
.nav-phone{display:flex;align-items:center;gap:6px;border:2px solid var(--ink);padding:4px 10px;font-size:17px;margin-left:4px}

/* hero */
.hero{top:108px;height:554px;background:linear-gradient(100deg,#5a3b22 0%,var(--hero-a) 35%,var(--hero-b) 75%,#c7ab86 100%)}
.hero-text{left:126px;top:150px;color:var(--white)}
.hero-text .welcome{font-size:32px;font-weight:500}
.hero-text h1{font-size:40px;font-weight:500;line-height:42px;margin-top:20px;letter-spacing:.5px}
.call-line{display:flex;align-items:center;gap:10px;margin-top:22px}
.call-ring{width:40px;height:40px;border:2px solid currentColor;border-radius:50%;display:flex;align-items:center;justify-content:center}
.call-line small{display:block;font-size:16px;line-height:18px}
.call-line b{font-weight:400;font-size:21px;line-height:24px}

/* about */
.about{top:662px;height:508px}
.about-shadow{left:144px;top:100px;width:400px;height:358px;background:linear-gradient(180deg,#2a2a2a,#8a8a8a)}
.about-photo{left:124px;top:94px;width:400px;height:340px;background:linear-gradient(135deg,#cfd6de,#7b8794 60%,#3f4d63)}
.about-copy{left:602px;top:92px;width:470px}
.about-copy .lead{font-family:"Montserrat",Arial,sans-serif;font-weight:600;font-size:18px}
.about-copy h2{font-family:"Montserrat",Arial,sans-serif;font-weight:500;font-size:30px;line-height:32px;margin-top:18px}
.about-copy p{font-size:16px;line-height:27px;margin-top:22px}
.about .btn-dark{left:602px;top:392px;width:160px;height:42px;font-size:18px}

/* services */
.services{top:1170px;height:852px;background:var(--soft)}
.section-title{position:absolute;left:0;width:1200px;text-align:center;font-family:"Montserrat",Arial,sans-serif;font-weight:500;font-size:30px;letter-spacing:1px}
.services .section-title{top:72px;word-spacing:6px}
.service-card{position:absolute;width:220px;height:264px;background:var(--white);box-shadow:0 2px 6px rgba(0,0,0,.18);text-align:center}
.service-photo{height:124px}
.service-badge{width:40px;height:40px;border-radius:50%;background:var(--white);margin:-22px auto 0;display:flex;align-items:center;justify-content:center;box-shadow:0 1px 3px rgba(0,0,0,.25);position:relative}
.service-card h3{font-family:"Open Sans",Arial,sans-serif;font-weight:600;font-size:14px;line-height:16px;margin-top:10px;height:34px;display:flex;align-items:center;justify-content:center}
.service-card .btn-dark{position:static;display:inline-flex;width:110px;height:26px;font-size:10px;font-weight:600;margin-top:6px}
.services .view-all{left:524px;top:758px;width:158px;height:46px;font-size:20px}

/* get started */
.cta-band{top:2024px;height:172px;background:linear-gradient(180deg,#2c3a4f 0%,#4a5565 55%,#6d6657 100%)}
.cta-band .title{left:222px;top:60px;font-size:30px;color:var(--white);font-weight:500}
.cta-band .call-line{position:absolute;left:534px;top:54px;margin:0;color:var(--white)}
.cta-band .call-line small{font-size:16px}
.quote-btn{position:absolute;left:780px;top:66px;width:200px;height:44px;background:var(--white);color:var(--ink);font-size:18px;display:flex;align-items:center;justify-content:center;font-family:"Montserrat",Arial,sans-serif}

/* process */
.process{top:2196px;height:592px}
.process h2{left:162px;top:92px;font-size:30px;font-weight:600}
.steps-line{left:189px;top:190px;height:280px;border-left:2px dotted #999}
.step{position:absolute;left:164px;width:420px}
.step-icon{position:absolute;left:0;top:0;width:52px;height:46px;background:var(--ink);border-radius:4px;display:flex;align-items:center;justify-content:center}
.step h3{margin-left:80px;font-family:"Montserrat",Arial,sans-serif;font-weight:500;font-size:21px}
.step p{margin-left:80px;margin-top:8px;font-size:13px;line-height:17px;color:#333;width:330px}
.process-frame{left:684px;top:90px;width:356px;height:438px;background:linear-gradient(180deg,#111,#8c8c8c)}
.process-photo{left:700px;top:100px;width:340px;height:416px;background:linear-gradient(180deg,#f1efea,#b7aa98 55%,#6f6558)}

/* recent projects */
.projects{top:2788px;height:408px;background:var(--black);color:var(--white)}
.projects h2{left:194px;top:66px;font-size:30px;font-weight:600;line-height:32px}
.projects p{left:194px;top:154px;width:200px;font-size:13px;font-weight:600;line-height:20px}
.portfolio-btn{position:absolute;left:190px;top:262px;width:202px;height:44px;background:var(--white);color:var(--ink);font-size:20px;display:flex;align-items:center;justify-content:center;font-family:"Montserrat",Arial,sans-serif}
.project-photo{top:64px;width:192px;height:268px}
.arrow{top:186px;color:var(--white)}

/* why choose us */
.why{top:3196px;height:640px;background:linear-gradient(90deg,#3d3b38 0%,#8d8a84 30%,#c9c5bd 55%,#9a938a 80%,#4b4640 100%)}
.why .section-title{top:60px;color:var(--white)}
.why-card{position:absolute;width:236px;height:226px;background:var(--white);text-align:center;padding-top:34px}
.why-icon{width:54px;height:48px;background:var(--ink);border-radius:4px;margin:0 auto;display:flex;align-items:center;justify-content:center}
.why-card h3{font-family:"Montserrat",Arial,sans-serif;font-weight:600;font-size:17px;margin-top:24px}
.why-card p{font-size:12px;line-height:15px;color:#444;width:190px;margin:12px auto 0}

/* clients */
.clients{top:3836px;height:424px}
.stars{position:absolute;left:0;width:1200px;text-align:center;top:64px;color:var(--star);font-size:14px;letter-spacing:2px}
.clients .section-title{top:92px;font-weight:700;font-size:30px}
.quote{position:absolute;top:160px;width:314px;height:124px;background:var(--black);color:var(--white);font-size:13px;line-height:16px;padding:30px 48px 0}
.quote::after{content:"";position:absolute;left:56px;bottom:-16px;border-left:16px solid transparent;border-right:16px solid transparent;border-top:16px solid var(--black)}
.client{position:absolute;top:306px;display:flex;align-items:center;gap:14px}
.avatar{width:48px;height:48px;border-radius:50%;background:linear-gradient(135deg,#dcdcdc,#555)}
.client b{display:block;color:var(--navy);font-size:13px;font-weight:700}
.client span{font-size:11px;color:#333}

/* contact */
.contact{top:4260px;height:580px}
.map{left:132px;top:40px;width:490px;height:424px;background:linear-gradient(135deg,#e9e6de,#dcd8cc 50%,#cfd6cf)}
.contact .brand{left:672px;top:116px;width:310px;justify-content:center;font-size:13px;letter-spacing:.5px;color:#555;gap:8px}
.contact .brand-square{width:11px;height:11px}
.contact .tagline{left:672px;top:144px;width:310px;text-align:center;font-size:10px;letter-spacing:1.5px;color:#888}
.info{position:absolute;left:694px;display:flex;gap:14px;align-items:flex-start;font-size:15px;line-height:24px;color:#222}
.info svg{margin-top:4px;flex:none}
.info.big{font-size:20px}

.divider{left:0;top:4790px;width:1200px;height:50px;background:linear-gradient(180deg,#ffffff,#cfcfcf 60%,#9a9a9a)}

/* footer */
.site-footer{top:4840px;height:292px;background:var(--black);color:var(--white)}
.footer-brand{position:absolute;left:160px;top:110px;width:180px;text-align:center;font-family:"Montserrat",Arial,sans-serif;font-weight:700;font-size:10px;line-height:14px;letter-spacing:.5px}
.footer-brand .brand-square{display:block;margin:0 auto 8px;background:var(--white);width:12px;height:12px}
.foot-contact{position:absolute;left:380px;top:92px;font-size:13px;line-height:30px}
.foot-contact div{display:flex;align-items:center;gap:12px}
.foot-col h4{font-family:"Montserrat",Arial,sans-serif;font-weight:600;font-size:14px;letter-spacing:.5px}
.quick{position:absolute;left:696px;top:72px}
.quick a{display:block;color:var(--white);text-decoration:none;font-size:12px;line-height:26px}
.quick h4{margin-bottom:8px}
.connect{position:absolute;left:888px;top:72px}
.socials{display:flex;gap:16px;margin-top:16px}
.socials span{width:20px;height:20px;border-radius:50%;background:var(--white)}
</style>
</head>
<body>
<svg width="0" height="0" style="position:absolute">
  <defs>
    <symbol id="phone" viewBox="0 0 24 24"><path fill="currentColor" d="M6.6 10.8a15 15 0 006.6 6.6l2.2-2.2a1 1 0 011-.25 11.4 11.4 0 003.6.57 1 1 0 011 1V20a1 1 0 01-1 1A17 17 0 013 4a1 1 0 011-1h3.5a1 1 0 011 1c0 1.250.2 2.450.57 3.570a1 1 0 01-.25 1z"/></symbol>
    <symbol id="house" viewBox="0 0 24 24"><path fill="currentColor" d="M12 3 2 12h3v8h5v-5h4v5h5v-8h3z"/></symbol>
    <symbol id="pin" viewBox="0 0 24 24"><path fill="none" stroke="currentColor" stroke-width="2" d="M12 22s7-7 7-12a7 7 0 00-14 0c0 5 7 12 7 12z"/><circle cx="12" cy="10" r="2.5" fill="none" stroke="currentColor" stroke-width="2"/></symbol>
    <symbol id="mail" viewBox="0 0 24 24"><rect x="3" y="5" width="18" height="14" fill="none" stroke="currentColor" stroke-width="2"/><path d="M3 6l9 7 9-7" fill="none" stroke="currentColor" stroke-width="2"/></symbol>
    <symbol id="clock" viewBox="0 0 24 24"><circle cx="12" cy="12" r="9" fill="none" stroke="currentColor" stroke-width="2"/><path d="M12 7v5l3 2" fill="none" stroke="currentColor" stroke-width="2"/></symbol>
  </defs>
</svg>

<header class="site-header">
  <div class="brand"><span class="brand-square"></span>Harlow &amp; Sons Construction Inc</div>
  <nav class="nav">
    <a href="#">HOME</a><a href="#">ABOUT US</a><a href="#">OUR SERVICES</a><a href="#">OUR WORK</a><a href="#">CONTACT US</a>
    <span class="nav-phone"><svg class="ico" width="18" height="18"><use href="#phone"/></svg>(555) 014-2290</span>
  </nav>
</header>

<section class="hero" role="img" aria-label="Photo of a bright renovated dining room with wooden table and leather chairs">
  <div class="abs hero-text head">
    <div class="welcome">Welcome to</div>
    <h1>HARLOW &amp; SONS<br>CONSTRUCTION INC</h1>
    <div class="call-line">
      <span class="call-ring"><svg class="ico" width="20" height="20"><use href="#phone"/></svg></span>
      <span><small>Call us today</small><b>(555) 014-0000</b></span>
    </div>
  </div>
</section>

<section class="about">
  <div class="abs about-shadow"></div>
  <div class="abs about-photo" role="img" aria-label="Photo of a smiling builder carrying timber planks"></div>
  <div class="abs about-copy">
    <div class="lead">Welcome to</div>
    <h2>HARLOW &amp; SONS<br>CONSTRUCTION INC</h2>
    <p>Lorem ipsum dolor sit amet consectetur. Nunc nam sed neque elit leo. Posuere ut enim suspendisse arcu amet eleifend mi consectetur. Hac in duis purus ac adipiscing id. Sagittis at tempus sollicitudin tincidunt. Urna nullam odio purus duis eu massa ligula. dit.</p>
  </div>
  <div class="btn-dark">Call us today</div>
</section>

<section class="services">
  <h2 class="section-title">OUR SERVICES</h2>

  <div class="service-card" style="left:124px;top:150px">
    <div class="service-photo" role="img" aria-label="Photo of a white house with dormers" style="background:linear-gradient(180deg,#a9c0d8,#e8e8e8 55%,#5f7d4a)"></div>
    <div class="service-badge"><svg class="ico" width="20" height="20"><use href="#house"/></svg></div>
    <h3>Dormers/Extensions</h3><div class="btn-dark">LEARN MORE</div>
  </div>
  <div class="service-card" style="left:368px;top:150px">
    <div class="service-photo" role="img" aria-label="Photo of a finished basement" style="background:linear-gradient(180deg,#efefef,#b9b3aa 60%,#6f655a)"></div>
    <div class="service-badge"><svg class="ico" width="20" height="20"><use href="#house"/></svg></div>
    <h3>Basement Remodel</h3><div class="btn-dark">LEARN MORE</div>
  </div>
  <div class="service-card" style="left:612px;top:150px">
    <div class="service-photo" role="img" aria-label="Photo of pavers being laid" style="background:linear-gradient(135deg,#c9ccd0,#8d949c 60%,#5a6068)"></div>
    <div class="service-badge"><svg class="ico" width="20" height="20"><use href="#house"/></svg></div>
    <h3>Masonry/Concrete/<br>Pavers/Asphalt</h3><div class="btn-dark">LEARN MORE</div>
  </div>
  <div class="service-card" style="left:858px;top:150px">
    <div class="service-photo" role="img" aria-label="Photo of a stone veneer house at dusk" style="background:linear-gradient(180deg,#6a7d99,#8b7a64 60%,#3e3a34)"></div>
    <div class="service-badge"><svg class="ico" width="20" height="20"><use href="#house"/></svg></div>
    <h3>Cultured Stone Veneer</h3><div class="btn-dark">LEARN MORE</div>
  </div>

  <div class="service-card" style="left:124px;top:446px">
    <div class="service-photo" role="img" aria-label="Photo of a modern kitchen" style="background:linear-gradient(180deg,#3b4652,#8a9aa5 55%,#d7d4cc)"></div>
    <div class="service-badge"><svg class="ico" width="20" height="20"><use href="#house"/></svg></div>
    <h3>Kitchens</h3><div class="btn-dark">LEARN MORE</div>
  </div>
  <div class="service-card" style="left:368px;top:446px">
    <div class="service-photo" role="img" aria-label="Photo of a bright bathroom" style="background:linear-gradient(180deg,#f1f1ef,#c9c4bc 60%,#8c857b)"></div>
    <div class="service-badge"><svg class="ico" width="20" height="20"><use href="#house"/></svg></div>
    <h3>Bathrooms</h3><div class="btn-dark">LEARN MORE</div>
  </div>
  <div class="service-card" style="left:612px;top:446px">
    <div class="service-photo" role="img" aria-label="Photo of a backyard pool with wooden fence" style="background:linear-gradient(180deg,#a55a3a,#c98a5e 45%,#3aa6c8)"></div>
    <div class="service-badge"><svg class="ico" width="20" height="20"><use href="#house"/></svg></div>
    <h3>Pool designs</h3><div class="btn-dark">LEARN MORE</div>
  </div>
  <div class="service-card" style="left:858px;top:446px">
    <div class="service-photo" role="img" aria-label="Photo of an outdoor bathroom" style="background:linear-gradient(180deg,#6b5d4b,#a08868 55%,#4f4637)"></div>
    <div class="service-badge"><svg class="ico" width="20" height="20"><use href="#house"/></svg></div>
    <h3>Outdoor Bathroom</h3><div class="btn-dark">LEARN MORE</div>
  </div>

  <div class="btn-dark view-all">VIEW ALL</div>
</section>

<section class="cta-band" role="img" aria-label="Photo of a shingled family house at dusk">
  <div class="abs title head">Get Started Today</div>
  <div class="call-line head">
    <span class="call-ring"><svg class="ico" width="20" height="20"><use href="#phone"/></svg></span>
    <span><small>Call us today</small><b>(555) 014-0000</b></span>
  </div>
  <div class="quote-btn">Request a quote</div>
</section>

<section class="process">
  <h2 class="abs head">OUR PROCESS</h2>
  <div class="abs steps-line"></div>
  <div class="step" style="top:156px">
    <div class="step-icon"><svg class="ico" width="24" height="24" viewBox="0 0 24 24"><rect x="5" y="3" width="14" height="18" fill="none" stroke="#fff" stroke-width="2"/><path d="M8 8h8M8 12h8M8 16h5" stroke="#fff" stroke-width="2"/></svg></div>
    <h3>Detailed Inspection &amp; Quote</h3>
    <p>Lorem ipsum dolor sit amet consectetur. Massa risus sapien consectetur aliquet gravida diam. Gravida interdum urna dui augue a tristique mattis malesuada.</p>
  </div>
  <div class="step" style="top:284px">
    <div class="step-icon"><svg class="ico" width="24" height="24"><use href="#house" style="color:#fff"/></svg></div>
    <h3>Brainstorming &amp; Design</h3>
    <p>Lorem ipsum dolor sit amet consectetur. Massa risus sapien consectetur aliquet gravida diam. Gravida interdum urna dui augue a tristique mattis malesuada.</p>
  </div>
  <div class="step" style="top:412px">
    <div class="step-icon"><svg class="ico" width="24" height="24" viewBox="0 0 24 24"><path d="M4 14a8 8 0 0116 0z" fill="#fff"/><rect x="3" y="14" width="18" height="3" fill="#fff"/></svg></div>
    <h3>Building &amp; Construction</h3>
    <p>Lorem ipsum dolor sit amet consectetur. Massa risus sapien consectetur aliquet gravida diam. Gravida interdum urna dui augue a tristique mattis malesuada.</p>
  </div>
  <div class="abs process-frame"></div>
  <div class="abs process-photo" role="img" aria-label="Photo of a living room with stone fireplace and timber beams"></div>
</section>

<section class="projects">
  <h2 class="abs head">OUR RECENT<br>PROJECTS</h2>
  <p class="abs">Looking for a 5 star home improvement company? Check out some of our recent projects!</p>
  <div class="portfolio-btn">More Portfolio</div>
  <svg class="abs arrow ico" style="left:436px" width="14" height="22" viewBox="0 0 14 22"><path d="M11 2 3 11l8 9" fill="none" stroke="currentColor" stroke-width="2"/></svg>
  <div class="abs project-photo" style="left:468px;background:linear-gradient(180deg,#e6ddcf,#a5744a 55%,#5a3a22)" role="img" aria-label="Photo of a renovated dining room"></div>
  <div class="abs project-photo" style="left:672px;background:linear-gradient(180deg,#7da3cf,#eeeeee 55%,#5b5b5b)" role="img" aria-label="Photo of a modern white house exterior"></div>
  <div class="abs project-photo" style="left:874px;background:linear-gradient(180deg,#9ab8d8,#8b5a38 45%,#8c8c84)" role="img" aria-label="Photo of an outdoor stone bathtub"></div>
  <svg class="abs arrow ico" style="left:1080px" width="14" height="22" viewBox="0 0 14 22"><path d="M3 2l8 9-8 9" fill="none" stroke="currentColor" stroke-width="2"/></svg>
</section>

<section class="why" role="img" aria-label="Photo of a softly lit living room">
  <h2 class="section-title">WHY CHOOSE US</h2>
  <div class="why-card" style="left:200px;top:112px"><div class="why-icon"><svg class="ico" width="24" height="24"><use href="#house" style="color:#fff"/></svg></div><h3>QUALITY OF WORK</h3><p>Praesent tempus at neque non hendrerit. In euismod vestibulum sodales.</p></div>
  <div class="why-card" style="left:482px;top:108px"><div class="why-icon"><svg class="ico" width="24" height="24"><use href="#house" style="color:#fff"/></svg></div><h3>EXPERIENCED TEAM</h3><p>Praesent tempus at neque non hendrerit. In euismod vestibulum sodales.</p></div>
  <div class="why-card" style="left:766px;top:116px"><div class="why-icon"><svg class="ico" width="24" height="24"><use href="#house" style="color:#fff"/></svg></div><h3>INNOVATION</h3><p>Praesent tempus at neque non hendrerit. In euismod vestibulum sodales.</p></div>
  <div class="why-card" style="left:200px;top:350px"><div class="why-icon"><svg class="ico" width="24" height="24"><use href="#house" style="color:#fff"/></svg></div><h3>INTEGRITY</h3><p>Praesent tempus at neque non hendrerit. In euismod vestibulum sodales.</p></div>
  <div class="why-card" style="left:482px;top:354px"><div class="why-icon"><svg class="ico" width="24" height="24"><use href="#house" style="color:#fff"/></svg></div><h3>FREE CONSULTATION</h3><p>Praesent tempus at neque non hendrerit. In euismod vestibulum sodales.</p></div>
  <div class="why-card" style="left:766px;top:354px"><div class="why-icon"><svg class="ico" width="24" height="24"><use href="#house" style="color:#fff"/></svg></div><h3>COMFORT</h3><p>Praesent tempus at neque non hendrerit. In euismod vestibulum sodales.</p></div>
</section>

<section class="clients">
  <div class="stars">★★★★★</div>
  <h2 class="section-title">OUR HAPPY CLIENTS!</h2>
  <div class="quote" style="left:132px">Lorem ipsum dolor sit amet, consectetur adipiscing elit, sed do eiusmod tempor incididunt ut labore et dolore magna aliqua.</div>
  <div class="quote" style="left:466px">Lorem ipsum dolor sit amet, consectetur adipiscing elit, sed do eiusmod tempor incididunt ut labore et dolore magna aliqua.</div>
  <div class="quote" style="left:792px">Lorem ipsum dolor sit amet, consectetur adipiscing elit, sed do eiusmod tempor incididunt ut labore et dolore magna aliqua.</div>
  <div class="client" style="left:172px"><div class="avatar" role="img" aria-label="Client portrait"></div><div><b>Dana Whitfield</b><span>Family Owner</span></div></div>
  <div class="client" style="left:506px"><div class="avatar" role="img" aria-label="Client portrait"></div><div><b>Dana Whitfield</b><span>Family Owner</span></div></div>
  <div class="client" style="left:832px"><div class="avatar" role="img" aria-label="Client portrait"></div><div><b>Dana Whitfield</b><span>Family Owner</span></div></div>
</section>

<section class="contact">
  <div class="abs map" role="img" aria-label="Street map showing the office location"></div>
  <div class="brand"><span class="brand-square" style="background:#555"></span>HARLOW &amp; SONS CONSTRUCTION INC</div>
  <div class="abs tagline">WE TREAT OUR CUSTOMERS LIKE FAMILY</div>
  <div class="info" style="top:206px"><svg class="ico" width="18" height="18"><use href="#pin"/></svg>Your address here</div>
  <div class="info big" style="top:244px"><svg class="ico" width="18" height="18"><use href="#phone"/></svg>(555) 014-0000</div>
  <div class="info" style="top:290px"><svg class="ico" width="18" height="18"><use href="#mail"/></svg>info@yourcompanyname.com</div>
  <div class="info" style="top:344px"><svg class="ico" width="18" height="18"><use href="#clock"/></svg><span>We're open Mon – Fri/7:00AM – 6:00PM.<br>Closed Saturday and Sunday.</span></div>
</section>

<div class="abs divider"></div>

<footer class="site-footer">
  <div class="footer-brand"><span class="brand-square"></span>HARLOW &amp; SONS<br>CONSTRUCTION INC</div>
  <div class="foot-contact">
    <div><svg class="ico" width="16" height="16"><use href="#pin"/></svg>Your location here</div>
    <div><svg class="ico" width="16" height="16"><use href="#mail"/></svg>info@harlowandsons.example</div>
    <div><svg class="ico" width="16" height="16"><use href="#phone"/></svg>(555) 014-7780</div>
  </div>
  <div class="foot-col quick">
    <h4>QUICKLINKS</h4>
    <a href="#">Home</a><a href="#">About Us</a><a href="#">Our Services</a><a href="#">Our Work</a><a href="#">Contact Us</a>
  </div>
  <div class="foot-col connect">
    <h4>CONNECTED WITH US</h4>
    <div class="socials"><span></span><span></span><span></span><span></span><span></span></div>
  </div>
</footer>
</body>
</html>
```